High-end construction company needs a business card design

We need a modern looking business card that draws people in, is memorable and looks so good people will want to sick it on their fridges.
On the first side what is needed are:
Logo
My name - Tomas Verbelk
Title - Managing Director
Website - www.kravel.co.uk
Email - tomas@kravel.co.uk
Telephone - 020 5194 6381
Mobile - 07845319027
On the back side was is needed is a list of all the services we provide:
-Kitchen Renovations
-Bathroom Renovations
-House Renovations
-Garage Conversions
-Extensions
-Loft Conversions
-Conservatories
-Carpentry
-Tiling
-Electrical
-Plumbing & Heating
-Bricklaying
-Landscaping
-Decorating
-Plastering
We would like the colours to be the same shades as on the logo with grey or black for the words.
Target Market(s)
Anyone who needs building work done
Contact Information for Business Card
This business card is for a construction company which strives to deliver excellent service and quality.
The look and feel of the card should represent this.
Requirements
Must have
- On the first side what is needed are:
Logo
My name - Tomas Verbelk
Title - Managing Director
Website - www.kravel.co.uk
Email - tomas@kravel.co.uk
Telephone - 020 5194 6381
Mobile - 07845319027
Nice to have
- Cool looking features

```html
<!DOCTYPE html>
<html lang="en">
<head>
<meta charset="UTF-8">
<title>Kravel Construction Ltd – Business Card</title>
<link href="https://fonts.googleapis.com/css2?family=Exo+2:wght@700;800&family=Poppins:wght@400;600;700&display=swap" rel="stylesheet">
<style>
  :root {
    --backdrop: #d7d7d7;
    --green-dark: #4a9440;
    --green-mid: #5aa83f;
    --green-light: #7cc243;
    --green-band: #3f8c3a;
    --ink: #1c1c1c;
    --ink-soft: #2e2e2e;
    --white: #ffffff;
  }
  * { margin: 0; padding: 0; box-sizing: border-box; }
  html, body { width: 1200px; height: 800px; overflow: hidden; }
  body { background: var(--backdrop); position: relative; }

  .card {
    position: absolute;
    top: 283px;
    width: 428px;
    height: 238px;
    overflow: hidden;
  }

  /* Services side */
  .card--services {
    left: 112px;
    background: linear-gradient(225deg, var(--green-light) 0%, var(--green-mid) 45%, var(--green-dark) 100%);
    color: var(--white);
    font-family: "Exo 2", sans-serif;
  }
  .services__title {
    position: absolute;
    left: 28px; top: 8px;
    font-size: 12px; font-weight: 800;
    letter-spacing: 0.4px;
  }
  .services__list {
    position: absolute;
    left: 30px; top: 26px;
    list-style: none;
  }
  .services__item {
    display: flex; align-items: center;
    height: 13.75px;
    font-size: 8.6px; font-weight: 800;
    letter-spacing: 0.5px;
  }
  .services__icon { width: 10px; height: 7px; margin-right: 3px; flex: none; }

  .brand {
    position: absolute;
    text-align: center;
    font-family: "Exo 2", sans-serif;
    font-weight: 800;
    line-height: 1;
  }
  .brand__name { display: block; font-size: 44px; letter-spacing: 1px; }
  .brand__tag { display: block; font-size: 10.5px; letter-spacing: 2.2px; margin-top: 3px; }
  .card--services .brand { left: 212px; top: 126px; width: 184px; color: var(--white); }

  /* Contact side */
  .card--contact {
    left: 638px;
    background: var(--white);
    font-family: "Poppins", sans-serif;
  }
  .card--contact .brand { left: 56px; top: 114px; width: 152px; color: var(--green-mid); }
  .card--contact .brand__name { font-size: 36px; }
  .card--contact .brand__tag { font-size: 8.6px; letter-spacing: 1.8px; }

  .person { position: absolute; left: 237px; top: 65px; }
  .person__name { font-size: 14px; font-weight: 700; color: var(--ink); letter-spacing: 0.2px; }
  .person__title {
    font-size: 10px; font-weight: 700; color: var(--green-mid);
    letter-spacing: 0.9px; margin-top: 1px;
  }
  .contact-list { list-style: none; margin-top: 11px; }
  .contact-list__item {
    display: flex; align-items: center;
    height: 14px;
    font-size: 10.5px; color: var(--ink-soft);
  }
  .contact-list__icon { width: 9px; height: 9px; margin: 0 8px 0 3px; flex: none; }

  .accent-band { position: absolute; left: 0; bottom: 0; width: 428px; height: 14px; }
</style>
</head>
<body>

<section class="card card--services" aria-label="Services side">
  <h2 class="services__title">SERVICES WE PROVIDE</h2>
  <ul class="services__list">
    <li class="services__item"><svg class="services__icon" viewBox="0 0 10 7"><path d="M0 7 L5 1 L10 7 M3 7 L5 4.5 L7 7" fill="none" stroke="#fff" stroke-width="1.4"/></svg>KITCHEN RENOVATIONS</li>
    <li class="services__item"><svg class="services__icon" viewBox="0 0 10 7"><path d="M0 7 L5 1 L10 7 M3 7 L5 4.5 L7 7" fill="none" stroke="#fff" stroke-width="1.4"/></svg>BATHROOM RENOVATIONS</li>
    <li class="services__item"><svg class="services__icon" viewBox="0 0 10 7"><path d="M0 7 L5 1 L10 7 M3 7 L5 4.5 L7 7" fill="none" stroke="#fff" stroke-width="1.4"/></svg>HOUSE RENOVATIONS</li>
    <li class="services__item"><svg class="services__icon" viewBox="0 0 10 7"><path d="M0 7 L5 1 L10 7 M3 7 L5 4.5 L7 7" fill="none" stroke="#fff" stroke-width="1.4"/></svg>GARAGE CONVERSIONS</li>
    <li class="services__item"><svg class="services__icon" viewBox="0 0 10 7"><path d="M0 7 L5 1 L10 7 M3 7 L5 4.5 L7 7" fill="none" stroke="#fff" stroke-width="1.4"/></svg>EXTENSIONS</li>
    <li class="services__item"><svg class="services__icon" viewBox="0 0 10 7"><path d="M0 7 L5 1 L10 7 M3 7 L5 4.5 L7 7" fill="none" stroke="#fff" stroke-width="1.4"/></svg>LOFT CONVERSIONS</li>
    <li class="services__item"><svg class="services__icon" viewBox="0 0 10 7"><path d="M0 7 L5 1 L10 7 M3 7 L5 4.5 L7 7" fill="none" stroke="#fff" stroke-width="1.4"/></svg>CONSERVATORIES</li>
    <li class="services__item"><svg class="services__icon" viewBox="0 0 10 7"><path d="M0 7 L5 1 L10 7 M3 7 L5 4.5 L7 7" fill="none" stroke="#fff" stroke-width="1.4"/></svg>CARPENTRY</li>
    <li class="services__item"><svg class="services__icon" viewBox="0 0 10 7"><path d="M0 7 L5 1 L10 7 M3 7 L5 4.5 L7 7" fill="none" stroke="#fff" stroke-width="1.4"/></svg>TILING</li>
    <li class="services__item"><svg class="services__icon" viewBox="0 0 10 7"><path d="M0 7 L5 1 L10 7 M3 7 L5 4.5 L7 7" fill="none" stroke="#fff" stroke-width="1.4"/></svg>ELECTRICAL</li>
    <li class="services__item"><svg class="services__icon" viewBox="0 0 10 7"><path d="M0 7 L5 1 L10 7 M3 7 L5 4.5 L7 7" fill="none" stroke="#fff" stroke-width="1.4"/></svg>PLUMBING &amp; HEATING</li>
    <li class="services__item"><svg class="services__icon" viewBox="0 0 10 7"><path d="M0 7 L5 1 L10 7 M3 7 L5 4.5 L7 7" fill="none" stroke="#fff" stroke-width="1.4"/></svg>BRICKLAYING</li>
    <li class="services__item"><svg class="services__icon" viewBox="0 0 10 7"><path d="M0 7 L5 1 L10 7 M3 7 L5 4.5 L7 7" fill="none" stroke="#fff" stroke-width="1.4"/></svg>LANDSCAPING</li>
    <li class="services__item"><svg class="services__icon" viewBox="0 0 10 7"><path d="M0 7 L5 1 L10 7 M3 7 L5 4.5 L7 7" fill="none" stroke="#fff" stroke-width="1.4"/></svg>DECORATING</li>
    <li class="services__item"><svg class="services__icon" viewBox="0 0 10 7"><path d="M0 7 L5 1 L10 7 M3 7 L5 4.5 L7 7" fill="none" stroke="#fff" stroke-width="1.4"/></svg>PLASTERING</li>
  </ul>
  <div class="brand">
    <span class="brand__name">KRAVEL</span>
    <span class="brand__tag">CONSTRUCTION LTD</span>
  </div>
</section>

<section class="card card--contact" aria-label="Contact side">
  <div class="brand">
    <span class="brand__name">KRAVEL</span>
    <span class="brand__tag">CONSTRUCTION LTD</span>
  </div>

  <div class="person">
    <h1 class="person__name">TOMAS VERBELK</h1>
    <p class="person__title">MANAGING DIRECTOR</p>
    <ul class="contact-list">
      <li class="contact-list__item">
        <svg class="contact-list__icon" viewBox="0 0 10 10"><path d="M2 0.5 L3.8 0.5 L4.4 3 L3.1 4 Q4.2 6 6 6.9 L7 5.6 L9.5 6.2 L9.5 8 Q9.5 9.5 8 9.5 Q0.5 9 0.5 2 Q0.5 0.5 2 0.5 Z" fill="#5aa83f"/></svg>
        020 5194 6381
      </li>
      <li class="contact-list__item">
        <svg class="contact-list__icon" viewBox="0 0 10 10"><rect x="2.3" y="0.5" width="5.4" height="9" rx="1" fill="none" stroke="#5aa83f" stroke-width="1.1"/><circle cx="5" cy="7.9" r="0.6" fill="#5aa83f"/></svg>
        07845319027
      </li>
      <li class="contact-list__item">
        <svg class="contact-list__icon" viewBox="0 0 10 10"><rect x="0.5" y="2" width="9" height="6.2" rx="0.6" fill="#5aa83f"/><path d="M0.8 2.4 L5 5.6 L9.2 2.4" fill="none" stroke="#fff" stroke-width="0.8"/></svg>
        tomas@kravel.co.uk
      </li>
      <li class="contact-list__item">
        <svg class="contact-list__icon" viewBox="0 0 10 10"><circle cx="5" cy="5" r="4.3" fill="none" stroke="#5aa83f" stroke-width="1"/><ellipse cx="5" cy="5" rx="1.9" ry="4.3" fill="none" stroke="#5aa83f" stroke-width="0.8"/><path d="M0.7 5 H9.3" stroke="#5aa83f" stroke-width="0.8"/></svg>
        www.kravel.co.uk
      </li>
    </ul>
  </div>

  <svg class="accent-band" viewBox="0 0 428 14" preserveAspectRatio="none" aria-hidden="true">
    <polygon points="0,7 214,7 210,14 0,14" fill="#6cb843"/>
    <polygon points="220,3 428,3 428,14 208,14" fill="#3f8c3a"/>
  </svg>
</section>

</body>
</html>
```